Bright Path Therapies business cards and stationary

Need business cards and stationary designed to match previously made logo for for a new company based in Sydney NSW called 'Bright Path Therapies'.

We provide early intervention services and diagnostic assessment for children with disability and their families. I would like designs that are colourful and child friendly - possibly using feet/footprints/steps on a white background. The final design should communicate that we are family friendly, accepting and fun to work with.

Target Market(s)

Parents and Families
Teachers
Allied Health Professionals

Industry/Entity Type

Psychology

Contact Information for Business Card

Bright Path Therapies
www.brightpaththerapies-example.com
info@brightpaththerapies-example.com

Font styles to use
Sans Serif
Decorative
Script

Requirements
Must have
• Match the font and colour scheme of logo, along with footprint picture
Nice to have
• Clean and simple, while reflecting that I am working with families.
• Also- editable for when we make staff specific cards.

```html
<!DOCTYPE html>
<html lang="en">
<head>
<meta charset="utf-8">
<title>Bright Path Therapies – Business Card</title>
<link href="https://fonts.googleapis.com/css2?family=Fredoka:wght@500&family=Roboto:wght@400;500;700&display=swap" rel="stylesheet">
<style>
  :root {
    --backdrop: #2b2b2b;
    --card-white: #f6f6f6;
    --brand-red: #e53e33;
    --brand-blue: #1f78c1;
    --brand-orange: #f28c1e;
    --brand-green: #8cc63f;
    --text-grey: #4a4a4a;
    --rule-grey: #9a9a9a;
    --print-soft: #f3d4d1;
  }
  * { box-sizing: border-box; margin: 0; padding: 0; }
  html, body { width: 1200px; height: 960px; overflow: hidden; }
  body {
    background: var(--backdrop);
    font-family: "Roboto", Arial, sans-serif;
    position: relative;
  }
  .card {
    position: absolute;
    width: 600px;
    height: 342px;
    border-radius: 20px;
    overflow: hidden;
  }
  /* Front */
  .card-front { left: 314px; top: 113px; background: var(--card-white); }
  .footprint-trail {
    position: absolute; left: 26px; top: 0; width: 190px; height: 320px;
    background: radial-gradient(ellipse at 30% 30%, var(--print-soft) 0%, rgba(243,212,209,0) 60%),
                radial-gradient(ellipse at 70% 70%, var(--print-soft) 0%, rgba(243,212,209,0) 60%);
    opacity: .7;
  }
  .brand-lockup {
    position: absolute; right: 32px; top: 48px;
    display: flex; align-items: center; gap: 12px;
  }
  .brand-mark { width: 40px; height: 40px; border-radius: 50%; background: var(--brand-red); }
  .brand-name {
    font-family: "Fredoka", "Roboto", sans-serif; font-weight: 500;
    font-size: 28px; color: var(--brand-blue); line-height: 1;
  }
  .person-name {
    position: absolute; left: 32px; top: 152px;
    font-family: "Fredoka", "Roboto", sans-serif; font-weight: 500;
    font-size: 26px; color: var(--brand-red); letter-spacing: .5px;
  }
  .person-role {
    position: absolute; left: 32px; top: 184px;
    font-size: 14px; font-weight: 700; color: var(--brand-blue);
  }
  .divider {
    position: absolute; left: 32px; top: 210px; width: 531px; height: 1px;
    background: var(--rule-grey);
  }
  .contact-list {
    position: absolute; left: 32px; top: 225px; list-style: none;
    font-size: 14.5px; color: var(--text-grey);
  }
  .contact-list li { display: flex; align-items: center; height: 19px; gap: 9px; }
  .contact-list svg { width: 13px; height: 13px; fill: var(--brand-red); flex: none; }
  .address {
    position: absolute; right: 30px; top: 240px; text-align: right;
    font-size: 14.5px; line-height: 19px; color: var(--text-grey);
    font-style: normal;
  }
  .colour-bands { position: absolute; left: 0; bottom: 0; width: 600px; height: 34px; }
  .web-address {
    position: absolute; right: 14px; bottom: 9px;
    font-size: 14px; color: #fff;
  }
  /* Back */
  .card-back {
    left: 311px; top: 472px; background: var(--brand-red);
    display: flex; flex-direction: column; align-items: center;
  }
  .back-lockup {
    margin-top: 124px; display: flex; align-items: center; gap: 18px;
  }
  .back-lockup .brand-mark { width: 60px; height: 60px; background: #fff; }
  .back-lockup .brand-name { font-size: 44px; color: #fff; }
  .tagline {
    margin-top: 66px; text-align: center; color: #fff;
    font-size: 14.5px; line-height: 19px;
  }
</style>
</head>
<body>
  <section class="card card-front">
    <div class="footprint-trail" role="img" aria-label="Faint trail of children's footprints"></div>

    <div class="brand-lockup">
      <span class="brand-mark"></span>
      <span class="brand-name">Bright Path Therapies</span>
    </div>

    <h1 class="person-name">ALEX CARTER</h1>
    <p class="person-role">CEO/FOUNDER</p>
    <div class="divider"></div>

    <ul class="contact-list">
      <li><svg viewBox="0 0 16 16"><path d="M3.6 1l2.6 3-1.5 1.8a9 9 0 0 0 5.5 5.5l1.8-1.5 3 2.6-1.7 2.4C7.5 14.7 1.3 8.5 1.2 2.7z"/></svg>612 555 0148</li>
      <li><svg viewBox="0 0 16 16"><path d="M4 0h8a1 1 0 0 1 1 1v14a1 1 0 0 1-1 1H4a1 1 0 0 1-1-1V1a1 1 0 0 1 1-1zm1 2v10h6V2zm3 11a1 1 0 1 0 0 2 1 1 0 0 0 0-2z"/></svg>614 555 0273</li>
      <li><svg viewBox="0 0 16 16"><path d="M4 0h8v4H4zM1 5h14v7h-2V9H3v3H1zm3 5h8v6H4z"/></svg>612 555 0391</li>
      <li><svg viewBox="0 0 16 16"><path d="M0 3h16v1.5L8 9 0 4.5zm0 3l8 4.5L16 6v7H0z"/></svg>info@brightpaththerapies-example.com</li>
    </ul>

    <address class="address">42 Wattle Street<br>Parramatta<br>NSW 2150</address>

    <svg class="colour-bands" viewBox="0 0 600 34" aria-hidden="true">
      <polygon points="0,15 118,15 112,23 0,23" fill="var(--brand-blue)"/>
      <polygon points="116,15 244,15 238,23 110,23" fill="var(--brand-orange)"/>
      <polygon points="248,15 358,15 352,23 242,23" fill="var(--brand-green)"/>
      <polygon points="0,23 600,23 600,34 0,34" fill="var(--brand-red)"/>
      <polygon points="372,0 600,0 600,34 342,34" fill="var(--brand-red)"/>
    </svg>
    <span class="web-address">brightpaththerapies-example.com</span>
  </section>

  <section class="card card-back">
    <div class="back-lockup">
      <span class="brand-mark"></span>
      <span class="brand-name">Bright Path Therapies</span>
    </div>
    <p class="tagline">Early intervention services &amp; diagnostic assessment<br>for children with disability and their families.</p>
  </section>
</body>
</html>
```